Plakat-Design für Vermieter von Ferienwohnungen im Allgäu
Zielgruppe
Wir vermieten Ferienwohnungen im Allgäu.
www.residenz-wiesental.de
Aufgabenstellung
Das Schild (Querformat) sollte freundlich, ansprechend und modern sein. Größe 140x180 cm.
Es wird eine Begrüßung für den Gast, wenn er in die Tiefgarage fährt.
Text:
Herzlich Willkommen
in der Residenz Lerchenau
Als Hintergrund können wir uns Berge, Landschaft oder ähnliches vorstellen.

```html
<!DOCTYPE html>
<html lang="de">
<head>
<meta charset="utf-8">
<title>Willkommen – Residenz Lerchenau</title>
<link href="https://fonts.googleapis.com/css2?family=Dancing+Script:wght@700&family=Mulish:wght@400&display=swap" rel="stylesheet">
<style>
  :root {
    --script-red: #a52f28;
    --paper: #ffffff;
    --ink: #1c1c1c;
    --meadow: #b9b45a;
    --meadow-deep: #6f7a3a;
    --hide-dark: #2a2a2e;
    --hide-tan: #b8a48e;
    --sky: #eef2f6;
  }
  * { margin: 0; padding: 0; box-sizing: border-box; }
  html, body {
    width: 1200px; height: 951px; overflow: hidden;
    background: var(--paper);
  }
  .sign {
    position: relative;
    width: 1200px; height: 951px;
    background: var(--paper);
  }
  .sign__backdrop {
    position: absolute; left: 0; top: 0;
    width: 1200px; height: 877px;
    background:
      radial-gradient(ellipse 360px 430px at 600px 470px, rgba(255,255,255,0.97) 0%, rgba(255,255,255,0.85) 55%, rgba(255,255,255,0) 100%),
      linear-gradient(90deg, var(--hide-tan) 0%, var(--hide-dark) 8%, var(--hide-tan) 18%, #d8cfc2 32%, var(--sky) 50%, #d9d9d9 68%, var(--hide-dark) 82%, #e8e6e2 92%, var(--hide-dark) 100%);
  }
  .sign__backdrop::after {
    content: ""; position: absolute; left: 0; right: 0; bottom: 0; height: 260px;
    background: linear-gradient(180deg, rgba(185,180,90,0) 0%, var(--meadow) 60%, var(--meadow-deep) 100%);
    opacity: 0.75;
  }
  .sign__brand {
    position: absolute; left: 0; width: 1200px; top: 120px;
    display: flex; justify-content: center; align-items: center; gap: 12px;
    font-family: "Dancing Script", cursive; font-weight: 700;
    font-size: 46px; color: var(--script-red);
  }
  .sign__brand-dot {
    width: 22px; height: 22px; border-radius: 50%;
    background: var(--script-red);
  }
  .sign__greeting {
    position: absolute; left: 0; width: 1200px; top: 258px;
    text-align: center;
    font-family: "Dancing Script", cursive; font-weight: 700;
    color: var(--script-red);
  }
  .sign__line { display: block; }
  .sign__line--large { font-size: 138px; line-height: 142px; }
  .sign__line--medium { font-size: 92px; line-height: 150px; }
  .sign__line--name { font-size: 122px; line-height: 118px; }
  .sign__footer {
    position: absolute; left: 0; top: 877px;
    width: 1200px; height: 74px;
    display: flex; align-items: center; justify-content: center;
    font-family: "Mulish", sans-serif; font-size: 26px;
    letter-spacing: 0.5px; color: var(--ink);
  }
</style>
</head>
<body>
  <main class="sign">
    <div class="sign__backdrop" role="img" aria-label="Foto: neugierige Kühe auf einer sonnigen Allgäuer Weide mit hohem Gras"></div>

    <div class="sign__brand">
      <span class="sign__brand-dot"></span>
      <span>Lerchenau</span>
    </div>

    <h1 class="sign__greeting">
      <span class="sign__line sign__line--large">Herzlich</span>
      <span class="sign__line sign__line--large">Willkommen</span>
      <span class="sign__line sign__line--medium">in der Residenz</span>
      <span class="sign__line sign__line--name">Lerchenau</span>
    </h1>

    <p class="sign__footer">PARKEN NUR FÜR GÄSTE DES WIESENWEG 12</p>
  </main>
</body>
</html>
```